2026 Kelvar Montra medium roof

Van montra logo wrap, construction company Bright Oak Renovations LLC

Target Market(s)

More customers

Industry/Entity Type

License contractor, remodeling, construction

Colors

Designer to choose colors to be used in the design.

Requirements
Must have
• House logo, jobs I offer, phone number,, license & insured , KLR acquitted business,
Nice to have
• I would like to have the KLR logo in lower right bottom of van

```html
<!DOCTYPE html>
<html lang="en">
<head>
<meta charset="utf-8">
<title>Bright Oak Renovations LLC – Kelvar Montra Van Wrap</title>
<link href="https://fonts.googleapis.com/css2?family=Poppins:wght@500;600;700;800&display=swap" rel="stylesheet">
<style>
  :root {
    --navy: #1d4a7c;
    --navy-dark: #163b64;
    --slate: #66788a;
    --slate-light: #a3adb6;
    --white: #ffffff;
    --body-white: #f4f5f6;
    --trim: #1c1d1f;
    --glass: #3b4147;
    --hub: #b9bec3;
    --tail: #c8262c;
  }
  html, body { margin: 0; padding: 0; width: 1200px; height: 1200px; overflow: hidden; background: var(--white); }
  .canvas { display: block; width: 1200px; height: 1200px; font-family: "Poppins", sans-serif; }
  .brand-name { font-weight: 700; fill: var(--navy); }
  .brand-sub { font-weight: 600; fill: var(--navy); }
  .phone { font-weight: 700; fill: var(--navy); }
  .license-no { font-weight: 600; fill: var(--trim); }
  .service-line { font-weight: 700; fill: var(--navy); }
  .service-item { font-weight: 600; fill: var(--white); }
  .website { font-weight: 600; fill: var(--white); }
  .trust-line { font-weight: 700; fill: var(--white); letter-spacing: .4px; }
  .mark-name { font-weight: 700; fill: var(--white); }
</style>
</head>
<body>
<svg class="canvas" viewBox="0 0 960 960" xmlns="http://www.w3.org/2000/svg">
  <defs>
    <path id="van-body" d="M60 300 Q70 272 120 250 Q170 200 215 150 Q300 108 385 102 L862 102 Q882 104 886 130 L890 392 L60 396 Z"/>
    <clipPath id="van-clip"><use href="#van-body"/></clipPath>
    <g id="van-base">
      <use href="#van-body" fill="var(--body-white)" stroke="#d4d7da" stroke-width="1"/>
      <path d="M60 352 L890 352 L890 400 L60 404 Z" fill="var(--trim)"/>
      <path d="M140 352 Q205 318 270 352 Z M670 352 Q735 318 800 352 Z" fill="var(--trim)"/>
      <path d="M230 164 L355 158 L355 250 L185 250 Z" fill="var(--glass)"/>
      <path d="M72 282 Q95 268 132 270 L128 300 L74 306 Z" fill="#9aa1a7"/>
      <rect x="868" y="245" width="18" height="85" rx="3" fill="var(--tail)"/>
      <line x1="360" y1="102" x2="360" y2="352" stroke="#c9cdd1" stroke-width="1"/>
      <line x1="598" y1="102" x2="598" y2="352" stroke="#c9cdd1" stroke-width="1"/>
      <circle cx="205" cy="402" r="48" fill="var(--trim)"/>
      <circle cx="205" cy="402" r="30" fill="var(--hub)"/>
      <circle cx="735" cy="402" r="48" fill="var(--trim)"/>
      <circle cx="735" cy="402" r="30" fill="var(--hub)"/>
    </g>
  </defs>

  <!-- Layout A: services listed under the name -->
  <g class="van van-layout-a">
    <use href="#van-base"/>
    <g clip-path="url(#van-clip)">
      <path class="rear-panel" d="M640 95 L900 95 L900 345 L620 345 Z" fill="var(--navy)"/>
      <path class="swoosh" d="M365 345 L365 330 Q365 300 400 300 L900 300 L900 345 Z" fill="var(--slate)"/>
    </g>
    <rect class="brand-square" x="705" y="135" width="80" height="80" fill="var(--slate-light)"/>
    <text class="mark-name" x="745" y="240" font-size="13" text-anchor="middle">BRIGHT OAK</text>
    <rect class="seal" x="832" y="276" width="26" height="46" rx="3" fill="var(--white)"/>
    <rect x="837" y="281" width="16" height="28" fill="var(--navy)"/>
    <text class="brand-name" x="385" y="194" font-size="22">BRIGHT OAK</text>
    <text class="brand-sub" x="385" y="217" font-size="16">RENOVATIONS LLC</text>
    <text class="service-line" x="395" y="262" font-size="6.2">KITCHENS &amp; BATHROOMS | DRYWALL &amp; PAINTING | PLUMBING &amp; ELECTRICAL</text>
    <text class="service-line" x="395" y="271" font-size="6.2">DOORS &amp; WINDOWS | FLOORING | INTERIOR &amp; EXTERIOR | ROOFING</text>
    <text class="service-line" x="395" y="280" font-size="6.2">SIDING | DECKS | FENCES</text>
    <text class="license-no" x="133" y="308" font-size="7.5">lic# 310045128</text>
    <text class="phone" x="225" y="303" font-size="18">(555) 014-2736</text>
    <circle cx="289" cy="326" r="7" fill="var(--slate)"/>
    <circle cx="313" cy="326" r="7" fill="var(--slate)"/>
    <text class="website" x="398" y="319" font-size="11">BrightOakRenovations.com</text>
    <rect class="trust-band" x="365" y="373" width="230" height="19" fill="var(--navy)"/>
    <text class="trust-line" x="400" y="387" font-size="10.5">LICENSED | INSURED | TRUSTED</text>
  </g>

  <!-- Layout B: services listed on the rear panel -->
  <g class="van van-layout-b" transform="translate(0 420)">
    <use href="#van-base"/>
    <g clip-path="url(#van-clip)">
      <path class="rear-panel" d="M690 95 L900 95 L900 345 L605 345 Z" fill="var(--navy)"/>
      <path class="accent-stripe" d="M664 95 L682 95 L598 345 L580 345 Z" fill="var(--slate)"/>
      <path class="swoosh" d="M365 345 L365 330 Q365 300 400 300 L640 300 L625 345 Z" fill="var(--slate)"/>
    </g>
    <rect class="brand-square" x="455" y="118" width="80" height="80" fill="var(--slate-light)"/>
    <text class="brand-name" x="495" y="264" font-size="19" text-anchor="middle">BRIGHT OAK</text>
    <text class="brand-sub" x="495" y="283" font-size="14" text-anchor="middle">RENOVATIONS LLC</text>
    <g class="service-list" font-size="11.5">
      <circle cx="700" cy="130" r="3" fill="var(--white)"/><text class="service-item" x="708" y="134">Kitchens &amp; bathrooms</text>
      <circle cx="700" cy="146" r="3" fill="var(--white)"/><text class="service-item" x="708" y="150">Drywall &amp; Painting</text>
      <circle cx="700" cy="162" r="3" fill="var(--white)"/><text class="service-item" x="708" y="166">Plumbing &amp; Electrical</text>
      <circle cx="700" cy="178" r="3" fill="var(--white)"/><text class="service-item" x="708" y="182">Doors &amp; Windows</text>
      <circle cx="700" cy="194" r="3" fill="var(--white)"/><text class="service-item" x="708" y="198">Flooring</text>
      <circle cx="700" cy="210" r="3" fill="var(--white)"/><text class="service-item" x="708" y="214">Interior &amp; exterior</text>
      <circle cx="700" cy="226" r="3" fill="var(--white)"/><text class="service-item" x="708" y="230">Roofing</text>
      <circle cx="700" cy="242" r="3" fill="var(--white)"/><text class="service-item" x="708" y="246">Siding</text>
      <circle cx="700" cy="258" r="3" fill="var(--white)"/><text class="service-item" x="708" y="262">Decks</text>
      <circle cx="700" cy="274" r="3" fill="var(--white)"/><text class="service-item" x="708" y="278">Fences</text>
    </g>
    <rect class="seal" x="808" y="256" width="38" height="56" rx="4" fill="var(--white)"/>
    <rect x="815" y="263" width="24" height="36" fill="var(--navy)"/>
    <text class="license-no" x="133" y="303" font-size="7.5">lic# 310045128</text>
    <text class="phone" x="225" y="301" font-size="18">(555) 014-2736</text>
    <circle cx="289" cy="325" r="7" fill="var(--slate)"/>
    <circle cx="313" cy="325" r="7" fill="var(--slate)"/>
    <text class="website" x="398" y="318" font-size="11">BrightOakRenovations.com</text>
    <rect class="trust-band" x="365" y="373" width="230" height="19" fill="var(--navy)"/>
    <text class="trust-line" x="400" y="387" font-size="10.5">LICENSED | INSURED | TRUSTED</text>
  </g>
</svg>
</body>
</html>
```